Innovation Presentation Template

I need a unique template design for a presentation on Innovation used exclusively inside of our company. I'd prefer to work in Apple Keynote but can take a .ppt and convert it. The template should appeal to a broad audience of diverse job descriptions. This is a one-time presentation that will last between 30 and 45 minutes. The design should provide a strong visual appeal with multiple chart layouts to support highlighted test points (no bullets, I hate bullets), graphics, line art, and video/photos. My presentations are sparse, never more that 2 concepts per chart (usually one). Our company is a high tech manufacturer selling products in many markets ranging from Government to consumer. The final design should include style a style guide including suggested fonts, colors, graph formats, suggested word art, etc.

Target Market(s)

The audience is internal employees only. Strong corporate branding is not required in this presentation.

Industry/Entity Type

Government

Colors
3277b5
faa54b

Requirements
Must have
• Strong visual appeal helping to support the communication of simple concepts (that have been broken down from complex subject matter).

Multiple chart template forms to support different forms of communication including text points, data charts, graphics, photos, and videos.

Visuals will be memorable, but not overpower the content. Visuals will help convey the content.

Well conceived and coordinated color pallets. Fonts guides (that I can access).

You can visit our company web site at www.KOVEX.com to see logo and corporate look/feel. It would be good to build logo into a few of the chart templates, but not all.
Nice to have
• Keynote (please). I can live with .ppt if I have to.

Many charts will make a point with simple single sentences. Find a way to make the sentences graphically interesting by varying font and/or color of specific words to help drive points.

Note that colors that I've identified below are based upon the blue used in our logo and the orange that complements it. I'm not married to these but use them as guidelines.
Should not have
• Noise. Corporate nauseia.

```html
<!DOCTYPE html>
<html lang="en">
<head>
<meta charset="utf-8">
<title>Project Title Here</title>
<link href="https://fonts.googleapis.com/css2?family=Ropa+Sans&display=swap" rel="stylesheet">
<style>
  :root {
    --blue-deep: #0b2fae;
    --blue-bright: #1f50d8;
    --blue-heading: #1450c8;
    --orange: #ffb000;
    --orange-light: #ffc21a;
    --slide-bg: #f3f5fb;
    --slide-bg-edge: #dde3f4;
    --ink: #111111;
    --white: #ffffff;
    --slice-silver: #c2c2c2;
    --slice-orange: #ffb000;
    --slice-sky: #3a70ef;
    --slice-royal: #0a63d9;
    --slice-charcoal: #5b5b5b;
    --slice-stone: #828282;
  }
  * { margin: 0; padding: 0; box-sizing: border-box; }
  html, body { width: 1200px; height: 900px; overflow: hidden; background: var(--white); }
  .slide {
    position: relative;
    width: 1200px;
    height: 900px;
    overflow: hidden;
    font-family: "Ropa Sans", sans-serif;
  }
  .backdrop {
    position: absolute; inset: 0;
    background:
      radial-gradient(ellipse 70% 55% at 30% 38%, var(--white) 0%, rgba(255,255,255,0) 70%),
      linear-gradient(180deg, var(--slide-bg) 0%, var(--slide-bg-edge) 100%);
  }
  .header-band {
    position: absolute; left: 0; top: 0; width: 1200px; height: 80px;
    background: linear-gradient(90deg, var(--blue-bright) 0%, var(--blue-deep) 60%, var(--blue-deep) 100%);
    border-bottom: 3px solid var(--orange);
  }
  .brand-tab {
    position: absolute; right: 0; top: 0; width: 270px; height: 80px;
    background: linear-gradient(180deg, var(--orange-light), var(--orange));
    clip-path: polygon(48px 0, 100% 0, 100% 100%, 0 100%);
    display: flex; align-items: center; justify-content: flex-end; gap: 12px;
    padding-right: 18px;
  }
  .brand-mark { width: 30px; height: 30px; background: var(--blue-deep); }
  .brand-name {
    font-family: "Ropa Sans", sans-serif;
    font-size: 46px; color: var(--blue-deep); letter-spacing: 1px;
  }
  .project-title {
    position: absolute; left: 26px; top: 10px;
    font-family: "Ropa Sans", sans-serif;
    font-weight: 400; font-size: 48px; line-height: 1.2; color: var(--white);
  }
  .content { position: absolute; left: 63px; top: 166px; width: 516px; }
  .content-heading {
    font-family: "Ropa Sans", sans-serif;
    font-weight: 400; font-size: 34px; line-height: 44px; color: var(--blue-heading);
    margin-bottom: 14px;
  }
  .content-paragraph {
    font-size: 24.5px; line-height: 36px; letter-spacing: 0.5px; color: var(--ink);
    text-align: justify; margin-bottom: 38px;
  }
  .pie-chart { position: absolute; left: 0; top: 0; width: 1200px; height: 900px; }
  .slice-label {
    font-family: "Ropa Sans", sans-serif;
    font-size: 18px; text-anchor: middle;
  }
  .label-light { fill: var(--white); }
  .label-dark { fill: var(--ink); }
  .footer-band {
    position: absolute; left: 0; bottom: 0; width: 1200px; height: 64px;
    background: linear-gradient(180deg, var(--orange-light), var(--orange));
    border-top: 2px solid var(--white);
  }
  .footer-blue {
    position: absolute; left: 0; bottom: 0; width: 330px; height: 64px;
    background: linear-gradient(90deg, var(--blue-deep), var(--blue-bright));
    clip-path: polygon(0 0, 100% 0, calc(100% - 48px) 100%, 0 100%);
  }
  .copyright {
    position: absolute; right: 14px; bottom: 10px;
    font-size: 22px; color: var(--ink);
  }
</style>
</head>
<body>
<main class="slide">
  <div class="backdrop" role="img" aria-label="Soft light blue background texture"></div>

  <header class="header-band">
    <h1 class="project-title">Project Title Here</h1>
    <div class="brand-tab">
      <span class="brand-mark"></span>
      <span class="brand-name">KOVEX</span>
    </div>
  </header>

  <section class="content">
    <h2 class="content-heading">Lorem ipsum dolor sit ipsum</h2>
    <p class="content-paragraph">Lorem ipsum dolor sit ipsum Lorem ipsum dolor sit ipsum Lorem ipsum dolor sit ipsum Lorem ipsum dolor sit ipsum lorem ipsum dolor sit ipsum Lorem ipsum dolor sit ipsum Lorem ipsum dolor sit ipsum</p>
    <p class="content-paragraph">Lorem ipsum dolor sit ipsum Lorem ipsum dolor sit ipsum Lorem ipsum dolor sit ipsum Lorem ipsum dolor sit ipsum</p>
    <p class="content-paragraph">Lorem ipsum dolor sit ipsum Lorem ipsum dolor sit ipsum Lorem ipsum dolor sit ipsum Lorem ipsum dolor sit ipsum</p>
  </section>

  <svg class="pie-chart" viewBox="0 0 1200 900" role="img" aria-label="Pie chart with six segments">
    <g stroke="#ffffff" stroke-width="1.5">
      <path d="M926 465 L926 233 A232 232 0 0 1 1062.4 277.3 Z" fill="var(--slice-silver)"/>
      <path d="M926 465 L1062.4 277.3 A232 232 0 0 1 1145.4 540.5 Z" fill="var(--slice-orange)"/>
      <path d="M926 465 L1145.4 540.5 A232 232 0 0 1 1009.1 681.6 Z" fill="var(--slice-sky)"/>
      <path d="M926 465 L1009.1 681.6 A232 232 0 0 1 706.6 540.5 Z" fill="var(--slice-royal)"/>
      <path d="M926 465 L706.6 540.5 A232 232 0 0 1 796.3 272.7 Z" fill="var(--slice-charcoal)"/>
      <path d="M926 465 L796.3 272.7 A232 232 0 0 1 926 233 Z" fill="var(--slice-stone)"/>
    </g>
    <circle cx="926" cy="465" r="37" fill="var(--orange)"/>
    <circle cx="926" cy="465" r="30" fill="var(--white)"/>

    <text class="slice-label label-dark"><tspan x="971" y="299">Lorem</tspan><tspan x="971" y="323">ipsum</tspan><tspan x="971" y="347">dolor</tspan></text>
    <text class="slice-label label-dark"><tspan x="1065" y="432">Lorem ipsum</tspan><tspan x="1065" y="455">dolor</tspan></text>
    <text class="slice-label label-dark"><tspan x="1036" y="558">Lorem ipsum</tspan><tspan x="1036" y="581">dolor</tspan></text>
    <text class="slice-label label-dark"><tspan x="863" y="571">Lorem ipsum dolor</tspan><tspan x="863" y="595">Lorem ipsum dolor</tspan></text>
    <text class="slice-label label-light"><tspan x="797" y="424">Lorem ipsum dolor</tspan><tspan x="797" y="448">Lorem ipsum dolor</tspan></text>
    <text class="slice-label label-light"><tspan x="882" y="299">Lorem</tspan><tspan x="882" y="323">ipsum</tspan><tspan x="882" y="347">dolor</tspan></text>
  </svg>

  <footer class="footer-band">
    <div class="footer-blue"></div>
    <p class="copyright">Copyright text here</p>
  </footer>
</main>
</body>
</html>
```